Psychologist in private practice needs a flyer and logo

We need a logo design and flyer design for my new private practice in Drummoyne. My company name is KBT Psychology, and my name is Leo Jane Harwick. I'm an experienced psychologist and have been registered since 2000. The final design should have a calm yet catchy theme, inviting clients rather than intimidating them, and should communicate wellbeing through therapy.

Target Market(s)

adolescents, young adults, population aged from 15-65. Targeting GPS also and wellness centres.

Industry/Entity Type

Psychology

Logo Text

KBT Psychology

Requirements
Must have
• Leo Jane Harwick, experienced psychologist registered since 2000. Is an Associate Member of the Kestrel Practitioners Guild. Has worked in Community Mental Health, Crisis teams, in the USA and in private practice since 2010.
• Is a registered Halvora Provider, and accepts most Private Health Funds. Also is a Tandem Assist approved provider.
• Email for bookings: kbtpsychology@quillpost.net phone 0472 318 605
• Practice address 1:
• Suite 4, 227 Kellaway Road
• Harlow Bay, NSW 2081
• Parking at rear on Beltane Street (near Tully Cafe)
• Penwick Medical Centre:
• Shop 5/38 Fenlow Rd, Ellery NSW 2196

```html
<!DOCTYPE html>
<html lang="en">
<head>
<meta charset="utf-8">
<title>KBT Psychology – Flyer</title>
<link href="https://fonts.googleapis.com/css2?family=Lato:wght@300;400;700;900&display=swap" rel="stylesheet">
<style>
  :root{
    --teal:#4fb6d3;
    --band:#5bbcd6;
    --green:#a9cc7c;
    --ink:#2b2b2b;
    --dark:#292929;
    --paper:#ffffff;
    --stage:#cfcfd3;
  }
  *{margin:0;padding:0;box-sizing:border-box}
  html,body{width:1200px;height:1200px;overflow:hidden}
  body{background:var(--stage);font-family:'Lato',sans-serif;color:var(--ink);position:relative}
  .flyer{position:absolute;top:55px;width:486px;height:1035px;background:var(--paper);overflow:hidden}
  .flyer--front{left:89px}
  .flyer--back{left:634px}
  .abs{position:absolute}

  /* brand */
  .brand{display:flex;align-items:center;gap:12px}
  .brand__dot{width:30px;height:30px;border-radius:50%;background:var(--green)}
  .brand__name{font-weight:700;color:var(--teal);font-size:40px;letter-spacing:1px;white-space:nowrap}
  .flyer--front .brand{left:0;right:0;top:58px;justify-content:center}

  /* hero */
  .hero{left:0;top:158px;width:486px;height:259px;
    background:linear-gradient(180deg,#e9e4d4 0%,#dfe0d3 38%,#6fb3b6 46%,#4e9ea7 62%,#b99a66 86%,#8f7446 100%)}
  .hero__title{left:44px;top:205px;font-weight:900;color:var(--teal);font-size:31px;line-height:37px;letter-spacing:-.5px}
  .hero__sub{left:45px;top:293px;width:250px;font-size:12.5px;line-height:17px;color:#fff;font-weight:400}

  .intro{left:48px;top:441px;width:390px;font-size:17px;line-height:21px}
  .conditions{left:48px;top:515px;list-style:none;font-size:17px;line-height:24px}
  .conditions li{position:relative;padding-left:31px}
  .conditions svg{position:absolute;left:1px;top:4px}

  .badge{left:296px;top:667px;width:148px;height:148px;border-radius:50%;background:#ececec;display:flex;align-items:center;justify-content:center;z-index:2}
  .badge__inner{width:134px;height:134px;border-radius:50%;background:var(--band);display:flex;flex-direction:column;align-items:center;justify-content:center;gap:10px}
  .badge__label{color:#fff;font-size:11.5px;line-height:14px;text-align:center}
  .badge__mark{width:48px;height:34px;border-radius:6px;background:#fff;opacity:.9}

  .bookings{left:0;width:486px;background:var(--band);color:#fff}
  .flyer--front .bookings{top:794px;height:93px;padding:14px 0 0 42px}
  .bookings__label{font-size:13.5px;text-decoration:underline;text-transform:uppercase}
  .bookings__line{font-size:20px;line-height:25px}
  .bookings__line b{font-weight:700}

  .footer{left:0;width:486px;background:var(--dark);color:#fff}
  .flyer--front .footer{top:887px;height:148px}
  .addr{font-size:13px;line-height:16.6px;white-space:nowrap}
  .addr__title{font-weight:700;text-decoration:underline}
  .addr--one{right:262px;top:29px;text-align:right}
  .addr--two{left:262px;top:29px}
  .footer__rule{left:241px;top:22px;width:3px;height:78px;background:var(--band)}

  /* back */
  .portrait{left:46px;top:59px;width:88px;height:108px;background:linear-gradient(160deg,#f1ece6,#b2876a 55%,#6b4735)}
  .about__title{left:158px;top:84px;font-weight:900;font-size:31px;color:var(--teal);line-height:34px}
  .about__name{left:158px;top:123px;font-weight:900;font-size:21px;line-height:24px;color:var(--teal);white-space:nowrap}
  .about__cred{left:158px;top:147px;font-size:16.5px;line-height:20px;color:var(--teal);font-weight:400}
  .copy{left:41px;width:410px;font-size:15px;line-height:17.3px;letter-spacing:-.3px}
  .copy p{margin-bottom:10px}
  .copy h2{font-weight:900;color:var(--teal);font-size:20.5px;line-height:24px;margin:34px 0 10px;letter-spacing:-.3px}
  .flyer--back .copy{top:182px}
  .flyer--back .bookings{top:693px;height:113px;text-align:center;padding-top:22px}
  .flyer--back .bookings__label{font-size:14.5px;margin-bottom:4px}
  .flyer--back .bookings__line{font-size:20.5px}
  .flyer--back .footer{top:806px;height:229px}
  .addr--back{left:41px;top:25px;font-size:14.4px;line-height:18.5px}
  .addr--back .addr__title{font-weight:400}
  .addr--back .big{font-size:17px;line-height:21px;margin-top:10px}
  .flyer--back .brand{left:300px;top:92px;gap:8px}
  .flyer--back .brand__dot{width:16px;height:16px}
  .flyer--back .brand__name{font-size:20px;letter-spacing:.3px}
</style>
</head>
<body>

<section class="flyer flyer--front">
  <div class="brand abs"><span class="brand__dot"></span><span class="brand__name">KBT Psychology</span></div>

  <div class="hero abs" role="img" aria-label="Photo of a woman in white sitting on a seaside rock looking out to sea"></div>
  <h1 class="hero__title abs">MENTAL HEALTH<br>FOR ALL!</h1>
  <p class="hero__sub abs">Specialised assessment, diagnosis and treatment of psychological problems and mental illness.</p>

  <p class="intro abs">Leo specialises in the assessment, diagnosis and treatment of psychological problems and mental illness including:</p>

  <ul class="conditions abs">
    <li><svg width="19" height="19" viewBox="0 0 20 20"><circle cx="10" cy="10" r="8.5" fill="none" stroke="#4fb6d3" stroke-width="2.2"/><path d="M6 10.3l2.8 2.7 5.2-5.5" fill="none" stroke="#4fb6d3" stroke-width="2.2" stroke-linecap="round" stroke-linejoin="round"/></svg>Depression and other mood disorders</li>
    <li><svg width="19" height="19" viewBox="0 0 20 20"><circle cx="10" cy="10" r="8.5" fill="none" stroke="#4fb6d3" stroke-width="2.2"/><path d="M6 10.3l2.8 2.7 5.2-5.5" fill="none" stroke="#4fb6d3" stroke-width="2.2" stroke-linecap="round" stroke-linejoin="round"/></svg>Anxiety disorders e.g. generalised anxiety,<br>social anxiety, panic attacks</li>
    <li><svg width="19" height="19" viewBox="0 0 20 20"><circle cx="10" cy="10" r="8.5" fill="none" stroke="#4fb6d3" stroke-width="2.2"/><path d="M6 10.3l2.8 2.7 5.2-5.5" fill="none" stroke="#4fb6d3" stroke-width="2.2" stroke-linecap="round" stroke-linejoin="round"/></svg>Adjustment to major life events or transitions<br>e.g. parenthood, divorce, retirement</li>
    <li><svg width="19" height="19" viewBox="0 0 20 20"><circle cx="10" cy="10" r="8.5" fill="none" stroke="#4fb6d3" stroke-width="2.2"/><path d="M6 10.3l2.8 2.7 5.2-5.5" fill="none" stroke="#4fb6d3" stroke-width="2.2" stroke-linecap="round" stroke-linejoin="round"/></svg>Loss, grief and bereavement</li>
    <li><svg width="19" height="19" viewBox="0 0 20 20"><circle cx="10" cy="10" r="8.5" fill="none" stroke="#4fb6d3" stroke-width="2.2"/><path d="M6 10.3l2.8 2.7 5.2-5.5" fill="none" stroke="#4fb6d3" stroke-width="2.2" stroke-linecap="round" stroke-linejoin="round"/></svg>Relationship difficulties</li>
    <li><svg width="19" height="19" viewBox="0 0 20 20"><circle cx="10" cy="10" r="8.5" fill="none" stroke="#4fb6d3" stroke-width="2.2"/><path d="M6 10.3l2.8 2.7 5.2-5.5" fill="none" stroke="#4fb6d3" stroke-width="2.2" stroke-linecap="round" stroke-linejoin="round"/></svg>Alcohol and drug misuse</li>
    <li><svg width="19" height="19" viewBox="0 0 20 20"><circle cx="10" cy="10" r="8.5" fill="none" stroke="#4fb6d3" stroke-width="2.2"/><path d="M6 10.3l2.8 2.7 5.2-5.5" fill="none" stroke="#4fb6d3" stroke-width="2.2" stroke-linecap="round" stroke-linejoin="round"/></svg>Stress</li>
    <li><svg width="19" height="19" viewBox="0 0 20 20"><circle cx="10" cy="10" r="8.5" fill="none" stroke="#4fb6d3" stroke-width="2.2"/><path d="M6 10.3l2.8 2.7 5.2-5.5" fill="none" stroke="#4fb6d3" stroke-width="2.2" stroke-linecap="round" stroke-linejoin="round"/></svg>Chronic pain</li>
    <li><svg width="19" height="19" viewBox="0 0 20 20"><circle cx="10" cy="10" r="8.5" fill="none" stroke="#4fb6d3" stroke-width="2.2"/><path d="M6 10.3l2.8 2.7 5.2-5.5" fill="none" stroke="#4fb6d3" stroke-width="2.2" stroke-linecap="round" stroke-linejoin="round"/></svg>Eating disorders</li>
  </ul>

  <div class="badge abs">
    <div class="badge__inner">
      <span class="badge__label">Registered<br>Member of</span>
      <span class="badge__mark" role="img" aria-label="Kestrel Practitioners Guild membership badge"></span>
    </div>
  </div>

  <div class="bookings abs">
    <div class="bookings__label">For Bookings</div>
    <div class="bookings__line">Email: <b>kbtpsychology@quillpost.net</b></div>
    <div class="bookings__line">Phone: <b>0472 318 605</b></div>
  </div>

  <div class="footer abs">
    <div class="addr addr--one abs">
      <div class="addr__title">Practice address 1</div>
      Suite 4, 227 Kellaway Road<br>Harlow Bay, NSW 2081<br>Parking at rear on Beltane Street
    </div>
    <div class="footer__rule abs"></div>
    <div class="addr addr--two abs">
      <div class="addr__title">Practice address 2</div>
      Penwick Medical Centre<br>&nbsp;Shop 5/38 Fenlow Rd,<br>Ellery NSW 2196
    </div>
  </div>
</section>

<section class="flyer flyer--back">
  <div class="portrait abs" role="img" aria-label="Portrait photo of Leo Jane Harwick"></div>
  <h2 class="about__title abs">ABOUT</h2>
  <div class="about__name abs">LEO JANE HARWICK</div>
  <div class="about__cred abs">BA (Psych), M Sports Psych</div>

  <div class="copy abs">
    <p>Leo has been a registered Psychologist since 2000. She is an Associate Member of the Kestrel Practitioners Guild (KPG) and is an approved Halvora provider and Tandem Assist provider. (BOLD)</p>
    <p>Leo's treatment modalities include Cognitive Behavioural Therapy, Mindfulness-based therapies, Acceptance and Commitment Therapy, Interpersonal Therapy and Solution Focussed Therapy. She tailors these evidence-based treatments to each client to help empower them to develop the tools and skills necessary to overcome challenges, with an encouraging and empathic approach.</p>
    <h2>WHY CHOOSE LEO?</h2>
    <p>Leo has over 16 years in providing therapy for a broad range of clients with a range of complexities. Since being in Private practice since 2010, Leo has grown to be a respected practitioner amongst her client base. She provides a non-judgmental and safe environment for clients to explore their difficulties and help them achieve their goals. She is able to establish good rapport and trust with children, adolescents adults and the elderly.</p>
    <p>Leo is an approved Halvora Provider which entitles you to a Halvora rebate if referred by a GP and she accepts most private health funds.</p>
    <p>Sessions are 50-60 minutes in duration.</p>
  </div>

  <div class="bookings abs">
    <div class="bookings__label">For Bookings</div>
    <div class="bookings__line">Email: <b>kbtpsychology@quillpost.net</b></div>
    <div class="bookings__line">Phone: <b>0472 318 605</b></div>
  </div>

  <div class="footer abs">
    <div class="addr addr--back abs">
      <div class="addr__title"><u>Practice address 1</u></div>
      Suite 4, 227 Kellaway Road<br>Harlow Bay, NSW 2081<br>Parking at rear on Beltane Street
      <div class="big"><u>Practice address 2</u><br>Penwick Medical Centre<br>&nbsp;Shop 5/38 Fenlow Rd,<br>Ellery NSW 2196</div>
    </div>
    <div class="brand abs"><span class="brand__dot"></span><span class="brand__name">KBT Psychology</span></div>
  </div>
</section>

</body>
</html>
```